Postcard Design- Market Update - April 2016

Real Estate Agent. I want to be able to enter data into a postcard (see attached) doesn't have to be exact, but similar and with similar info. I did one postcard with this company already - it may help to see the back of it for how i laid it out.

Target Market(s)

Luxury homes - 800,000- 3,000,000

Industry/Entity Type

Real Estate Agent

Requirements
Must have
• Need to be able to edit the 5 data fields. This is for a luxury market...so it can be a little fanicer.

```html
<!DOCTYPE html>
<html lang="en">
<head>
<meta charset="utf-8">
<title>Crestview Market Update Postcard</title>
<link href="https://fonts.googleapis.com/css2?family=Montserrat:wght@700;800&family=Roboto:wght@700&display=swap" rel="stylesheet">
<style>
  :root {
    --red: #ee1c24;
    --ink: #111111;
    --grey: #b5b5b5;
    --paper: #ffffff;
    --dusk-sky: #3f5f86;
    --warm-light: #c98a3e;
    --stone: #6e6a66;
    --pool: #4a4fa8;
  }
  * { margin: 0; padding: 0; box-sizing: border-box; }
  html, body { width: 1200px; height: 840px; overflow: hidden; background: var(--paper); }
  .canvas { position: relative; width: 1200px; height: 840px; }

  .postcard {
    position: absolute; left: 328px; width: 569px; height: 370px;
    background: var(--paper); overflow: hidden;
    box-shadow: 2px 3px 6px rgba(0,0,0,.35);
  }
  .postcard--front { top: 34px; }
  .postcard--back { top: 442px; height: 367px; }

  .front-art { position: absolute; inset: 0; width: 100%; height: 100%; }

  .badge {
    position: absolute; left: 332px; top: 20px; width: 53px; height: 53px;
    border-radius: 50%; background: var(--grey);
    display: flex; align-items: center; justify-content: center;
    font: 800 20px/1 "Montserrat", sans-serif; color: var(--ink);
  }
  .headline {
    position: absolute; left: 392px; top: 29px;
    font: 700 20px/24px "Montserrat", sans-serif; color: var(--ink);
    text-transform: uppercase;
  }

  .stat { position: absolute; left: 0; top: 0; }
  .stat-icon { position: absolute; left: 341px; width: 38px; height: 38px; }
  .stat-value {
    position: absolute; left: 390px; height: 3px;
    border-bottom: 3px dotted var(--ink);
  }
  .stat-label {
    position: absolute; left: 390px;
    font: 700 12px/1 "Roboto", sans-serif; color: var(--red); white-space: nowrap;
  }

  .photo-stack { position: absolute; left: 0; top: 0; width: 348px; }
  .photo { display: block; width: 348px; }
  .photo--manor { height: 114px; background: linear-gradient(180deg, #6f8db3 0%, #b9a07a 55%, #3b3a2e 100%); }
  .photo--lodge { height: 130px; background: linear-gradient(180deg, #3e5f8a 0%, #6a4b33 50%, #c98a3e 75%, #2e3a2a 100%); }
  .photo--villa { height: 89px; background: linear-gradient(180deg, #c8cfd6 0%, #e6e2da 45%, #8c8f7c 100%); }

  .contact-bar {
    position: absolute; left: 0; top: 333px; width: 348px; height: 34px;
    background: var(--red); padding-left: 12px;
    display: flex; align-items: center; gap: 6px;
    font: 800 16px/1 "Montserrat", sans-serif; color: var(--paper);
  }
  .contact-line { width: 160px; border-bottom: 3px dotted var(--paper); transform: translateY(3px); }

  .address-lines { position: absolute; left: 396px; top: 185px; }
  .address-line { width: 136px; height: 25px; border-bottom: 3px dotted var(--ink); }
  .address-line:first-child { height: 3px; margin-bottom: 22px; }
  .address-lines .address-line + .address-line { height: 25px; }
</style>
</head>
<body>
<div class="canvas">

  <section class="postcard postcard--front">
    <svg class="front-art" viewBox="0 0 569 370" preserveAspectRatio="none" aria-hidden="false">
      <defs>
        <linearGradient id="estateDusk" x1="0" y1="0" x2="0" y2="1">
          <stop offset="0" stop-color="#3f5f86"/>
          <stop offset="0.35" stop-color="#4a4a55"/>
          <stop offset="0.62" stop-color="#c98a3e"/>
          <stop offset="0.85" stop-color="#6e6a66"/>
          <stop offset="1" stop-color="#4a4fa8"/>
        </linearGradient>
      </defs>
      <polygon points="244,0 252,0 342,176 266,370 258,370 334,176" fill="var(--red)"/>
      <polygon points="0,0 244,0 334,176 258,370 0,370" fill="url(#estateDusk)" role="img" aria-label="Photograph of a luxury home lit at dusk with a pool in front"/>
    </svg>

    <div class="badge">Q?</div>
    <h1 class="headline">Crestview Market<br>Update</h1>

    <div class="stat">
      <svg class="stat-icon" style="top:88px" viewBox="0 0 40 40"><path d="M4 20 L20 6 L36 20 L36 34 L4 34 Z" fill="var(--ink)"/><rect x="27" y="7" width="5" height="9" fill="var(--ink)"/><path d="M14 30 V22 h3 l3-6 q2 0 2 3 v2 h5 q2 0 2 2 l-1 5 q-1 2-3 2 Z" fill="var(--paper)"/></svg>
      <div class="stat-value" style="top:103px;width:86px"></div>
      <div class="stat-label" style="top:115px">Closed Deals</div>
    </div>
    <div class="stat">
      <svg class="stat-icon" style="top:145px" viewBox="0 0 40 40"><path d="M8 12 A14 14 0 1 0 20 6" fill="none" stroke="var(--ink)" stroke-width="3.5"/><path d="M20 2 L26 6 L20 10 Z" fill="var(--ink)"/><path d="M20 13 V21 L14 26" fill="none" stroke="var(--ink)" stroke-width="3.5"/></svg>
      <div class="stat-value" style="top:160px;width:152px"></div>
      <div class="stat-label" style="top:172px">Average Days on Market</div>
    </div>
    <div class="stat">
      <svg class="stat-icon" style="top:200px" viewBox="0 0 40 40"><text x="20" y="33" text-anchor="middle" font-family="Montserrat, sans-serif" font-weight="700" font-size="34" fill="var(--ink)">$</text></svg>
      <div class="stat-value" style="top:215px;width:98px"></div>
      <div class="stat-label" style="top:227px">Average Sale Price</div>
    </div>
    <div class="stat">
      <svg class="stat-icon" style="top:256px" viewBox="0 0 40 40"><path d="M20 3 L12 12 M20 3 L28 12" stroke="var(--ink)" stroke-width="2" fill="none"/><rect x="4" y="12" width="32" height="22" fill="var(--ink)" transform="rotate(-6 20 23)"/><text x="20" y="28" text-anchor="middle" font-family="Roboto, sans-serif" font-size="10" font-weight="700" fill="var(--paper)" transform="rotate(-6 20 23)">SALE</text></svg>
      <div class="stat-value" style="top:271px;width:98px"></div>
      <div class="stat-label" style="top:283px">Homes for Sale</div>
    </div>
    <div class="stat">
      <svg class="stat-icon" style="top:311px" viewBox="0 0 40 40"><rect x="7" y="4" width="26" height="32" rx="4" fill="none" stroke="var(--ink)" stroke-width="3.5"/><path d="M13 20 L20 14 L27 20 V28 H13 Z" fill="var(--ink)"/></svg>
      <div class="stat-value" style="top:326px;width:128px"></div>
      <div class="stat-label" style="top:338px">Average Home Price</div>
    </div>
  </section>

  <section class="postcard postcard--back">
    <div class="photo-stack">
      <div class="photo photo--manor" role="img" aria-label="Photograph of a stone manor house at dusk"></div>
      <div class="photo photo--lodge" role="img" aria-label="Photograph of a gabled luxury home with lit windows"></div>
      <div class="photo photo--villa" role="img" aria-label="Photograph of a white villa with balconies"></div>
    </div>
    <div class="contact-bar">CONTACT <span class="contact-line"></span></div>

    <div class="address-lines">
      <div class="address-line"></div>
      <div class="address-line"></div>
      <div class="address-line"></div>
      <div class="address-line"></div>
      <div class="address-line"></div>
    </div>
  </section>

</div>
</body>
</html>
```